Design a helpdesk ticketing platform *

We are launching a helpdesk ticketing platform. Very much like quellbox.com, merrylark.com, pivolta.com, brisktray.com etc. We have a full mid-fidelity prototype built and we want someone to build the full fidelity of the product.

You can view the full mid-fidelity prototype here: https://lnk.vexora.net/Qa8Lpw

The best way moving forward is to just design the following 4 pages

- Main Dashboard https://lnk.vexora.net/81hRtd
- All tickets https://lnk.vexora.net/jwNoEb
- Viewing a ticket https://lnk.vexora.net/Ys4VmK
- Contacts https://lnk.vexora.net/pHeXuo

Target Market(s)

Small business owners

Industry/Entity Type

Saas

Number of Pages Required

4 page

Font styles to use
Serif
Sans Serif

Colors

Designer to choose colors to be used in the design.

Requirements
Must have
• Must follow the prototype exactly. We are not looking for any UX changes. We want the designe xactly as the prototype is. We are only looking for design ideas.
Should not have
• modern, clean. We'd love to see the primary color as yellow, purple, orange, green or blue. You choose which one you think looks best and go with that.

```html
<!DOCTYPE html>
<html lang="en">
<head>
<meta charset="utf-8">
<title>deskharbor – Dashboard</title>
<link href="https://fonts.googleapis.com/css2?family=Lato:wght@300;400;700&display=swap" rel="stylesheet">
<style>
:root{
  --brand:#f0483e;
  --sidebar:#2c3640;
  --sidebar-line:#232b33;
  --active:#29a8e0;
  --page:#f4f5f7;
  --white:#ffffff;
  --text:#333a40;
  --muted:#555d64;
  --line:#dcdfe2;
  --search-btn:#2cb673;
  --avatar:#e0457b;
  --arrow:#29a8e0;
  --donut-yellow:#f9c23c;
  --donut-slate:#5b7a93;
  --t-blue:#2f5faa;
  --t-green:#4aa64a;
  --t-orange:#dc4f2c;
  --t-yellow:#f7b23f;
  --t-red:#f14a4a;
  --t-purple:#8e3a8c;
}
*{box-sizing:border-box;margin:0;padding:0}
html,body{width:1200px;height:786px;overflow:hidden}
body{font-family:'Lato',sans-serif;background:var(--page);color:var(--text);position:relative}
.sidebar{position:absolute;left:0;top:0;width:173px;height:786px;background:var(--sidebar)}
.logo{height:51px;background:var(--brand);color:var(--white);font-size:21px;display:flex;align-items:center;justify-content:center;font-weight:400}
.nav{margin-top:16px;list-style:none}
.nav li{height:52px;border-bottom:1px solid var(--sidebar-line);display:flex;align-items:center;padding-left:25px;color:var(--white);font-size:12.5px;gap:12px}
.nav li.active{background:var(--active);font-weight:700}
.nav svg{width:16px;height:16px;flex:none}
.caret{font-size:9px;margin-left:4px}
.topbar{position:absolute;left:173px;top:0;right:0;height:52px;background:var(--white);border-bottom:1px solid var(--line)}
.menu-toggle{position:absolute;left:21px;top:20px}
.search{position:absolute;left:732px;top:10px;width:196px;height:30px;display:flex}
.search input{flex:1;border:1px solid #ccc;border-right:none;background:#f2f2f2;font:13px 'Lato',sans-serif;padding-left:14px;color:#555}
.search button{width:31px;border:none;background:var(--search-btn);display:flex;align-items:center;justify-content:center}
.avatar{position:absolute;left:943px;top:9px;width:34px;height:34px;border-radius:50%;background:var(--avatar);color:var(--white);font-size:12.5px;font-weight:700;display:flex;align-items:center;justify-content:center}
.more{position:absolute;left:993px;top:21px}
.greeting{position:absolute;left:193px;top:68px;font-size:32px;font-weight:300;color:#333}
.tiles{position:absolute;left:192px;top:118px;display:flex;gap:15px}
.tile{width:152px;height:99px;color:var(--white);display:flex;flex-direction:column;align-items:center;padding-top:14px;text-shadow:0 1px 1px rgba(0,0,0,.2)}
.tile .num{font-size:42px;font-weight:300;line-height:1.05}
.tile .label{font-size:12.5px;margin-top:4px}
.panel{position:absolute;left:192px;top:249px;width:987px;height:528px;background:var(--white);border:1px solid var(--line)}
.panel h2{position:absolute;left:18px;top:15px;font-size:21px;font-weight:400}
.panel .rule{position:absolute;left:18px;right:18px;top:51px;border-top:1px solid #888}
.group{position:absolute;left:0;right:0}
.donut{position:absolute;left:18px;top:0;width:38px;height:38px}
.stem{position:absolute;left:36px;border-left:1px solid var(--line)}
.day{position:absolute;left:77px;top:8px;font-size:16px}
.entries{position:absolute;left:80px;right:18px;list-style:none}
.entries li{height:62px;border-bottom:1px solid var(--line);padding:8px 0 0 25px;position:relative}
.entries li svg{position:absolute;left:0;top:11px}
.time{font-size:12px;color:var(--muted)}
.time b{color:var(--text)}
.desc{font-size:14px;margin-top:3px}
</style>
</head>
<body>
<aside class="sidebar">
  <div class="logo">deskharbor</div>
  <ul class="nav">
    <li><svg viewBox="0 0 16 16" fill="none" stroke="#fff" stroke-width="1.2"><path d="M1 8l14-6-5 13-3-5z"/><path d="M7 10l8-8"/></svg>New Tickets <svg viewBox="0 0 16 16" stroke="#fff" stroke-width="2" style="width:13px"><path d="M1 3h14M1 8h14M1 13h14"/></svg></li>
    <li class="active"><svg viewBox="0 0 16 16" fill="none" stroke="#fff" stroke-width="1.2"><path d="M8 1l2.1 4.6 5 .5-3.8 3.3 1.1 5L8 11.8 3.6 14.4l1.1-5L.9 6.1l5-.5z"/></svg>Dashboard</li>
    <li><svg viewBox="0 0 16 16" fill="none" stroke="#fff" stroke-width="1.2"><path d="M1 8l14-6-5 13-3-5z"/><path d="M7 10l8-8"/></svg>Tickets <span class="caret">▼</span></li>
    <li><svg viewBox="0 0 16 16" fill="none" stroke="#fff" stroke-width="1.2"><circle cx="8" cy="5" r="3.2"/><path d="M1.5 15c0-3.5 3-5.5 6.5-5.5s6.5 2 6.5 5.5z"/></svg>Contacts</li>
    <li><svg viewBox="0 0 16 16" fill="none" stroke="#fff" stroke-width="1.2"><circle cx="8" cy="8" r="2.5"/><circle cx="8" cy="8" r="5.5" stroke-dasharray="2 1.5"/></svg>Admin Settings <span class="caret">▼</span></li>
    <li><svg viewBox="0 0 16 16" fill="none" stroke="#fff" stroke-width="1.2"><rect x="1" y="3.5" width="14" height="9" rx="1"/><path d="M1 6.5h14M3 10h4"/></svg>Account &amp; Billing</li>
  </ul>
</aside>

<header class="topbar">
  <svg class="menu-toggle" width="16" height="12" viewBox="0 0 16 12" stroke="#f0483e" stroke-width="1.6"><path d="M0 2h13M0 6h11M0 10h13M15 2h1M15 6h1M15 10h1"/></svg>
  <form class="search"><input type="text" placeholder="Search"><button type="button" aria-label="Search"><svg width="12" height="12" viewBox="0 0 12 12" fill="none" stroke="#fff" stroke-width="2"><circle cx="5" cy="5" r="3.6"/><path d="M7.8 7.8L11 11"/></svg></button></form>
  <div class="avatar">MR</div>
  <svg class="more" width="14" height="11" viewBox="0 0 14 11" stroke="#f0483e" stroke-width="1.6"><path d="M0 1h14M0 5.5h14M0 10h14"/></svg>
</header>

<h1 class="greeting">Good Morning, Marcus</h1>

<section class="tiles">
  <div class="tile" style="background:var(--t-blue)"><span class="num">16</span><span class="label">Open Tickets</span></div>
  <div class="tile" style="background:var(--t-green)"><span class="num">14</span><span class="label">Due Today</span></div>
  <div class="tile" style="background:var(--t-orange)"><span class="num">14</span><span class="label">Unassigned</span></div>
  <div class="tile" style="background:var(--t-yellow)"><span class="num">0</span><span class="label">Over Due</span></div>
  <div class="tile" style="background:var(--t-red)"><span class="num">0</span><span class="label">On Hold</span></div>
  <div class="tile" style="background:var(--t-purple)"><span class="num">11</span><span class="label">Not Resolved</span></div>
</section>

<section class="panel">
  <h2>Recent Activities</h2>
  <div class="rule"></div>

  <div class="group" style="top:76px">
    <svg class="donut" viewBox="0 0 38 38"><circle cx="19" cy="19" r="13" fill="none" stroke="var(--donut-yellow)" stroke-width="10"/><circle cx="19" cy="19" r="13" fill="none" stroke="var(--donut-slate)" stroke-width="10" stroke-dasharray="16 82" transform="rotate(-90 19 19)"/><path d="M32 19h6" stroke="#fff" stroke-width="3"/></svg>
    <div class="stem" style="top:44px;height:150px"></div>
    <div class="day">Today</div>
    <ul class="entries" style="top:21px">
      <li><svg width="19" height="12" viewBox="0 0 19 12" fill="var(--arrow)"><path d="M0 4.5h12V0l7 6-7 6V7.5H0z"/></svg><div class="time"><b>4:49</b> pm</div><div class="desc">Daniel Koh assigned forgot to cc, trying again (#15) to Daniel Koh.</div></li>
      <li><svg width="19" height="12" viewBox="0 0 19 12" fill="var(--arrow)"><path d="M0 4.5h12V0l7 6-7 6V7.5H0z"/></svg><div class="time"><b>10:49</b> am</div><div class="desc">Daniel Koh assigned forgot to cc, trying again (#15) to Daniel Koh.</div></li>
      <li><svg width="19" height="12" viewBox="0 0 19 12" fill="var(--arrow)"><path d="M0 4.5h12V0l7 6-7 6V7.5H0z"/></svg><div class="time"><b>9:49</b> am</div><div class="desc">Daniel Koh added a note to the ticket Test From Email (#12)</div></li>
    </ul>
  </div>

  <div class="group" style="top:310px">
    <svg class="donut" viewBox="0 0 38 38"><circle cx="19" cy="19" r="13" fill="none" stroke="var(--donut-yellow)" stroke-width="10"/><circle cx="19" cy="19" r="13" fill="none" stroke="var(--donut-slate)" stroke-width="10" stroke-dasharray="16 82" transform="rotate(-90 19 19)"/><path d="M32 19h6" stroke="#fff" stroke-width="3"/></svg>
    <div class="stem" style="top:44px;height:100px"></div>
    <div class="day">Yesterday</div>
    <ul class="entries" style="top:21px">
      <li><svg width="19" height="12" viewBox="0 0 19 12" fill="var(--arrow)"><path d="M0 4.5h12V0l7 6-7 6V7.5H0z"/></svg><div class="time"><b>5:49</b> pm</div><div class="desc">Daniel Koh assigned test (#15)</div></li>
      <li><svg width="19" height="12" viewBox="0 0 19 12" fill="var(--arrow)"><path d="M0 4.5h12V0l7 6-7 6V7.5H0z"/></svg><div class="time"><b>12:00</b> pm</div><div class="desc">Lim Wei Shan raised a new ticket test (#16)</div></li>
    </ul>
  </div>
</section>
</body>
</html>
```